I Need a New Design For Existing Wordpress Site

My website is www.fretmorningacademy.example. The purpose is to provide free guitar lessons. Each blog post is a new video lesson embedded from ClipStreamo. The site is also an avenue to sell my ebook.

I need a Wordpress design that is appealing and professional. It should make the user feel as if the site is legitimate and trustworthy. I like the color schemes that use blues, grey,s and white matching my logo.

Examples of website designs I like:
www.strumvelta.example
www.pinehavenworks.example
www.steadyyieldnotes.example

Target Market(s)

15-35 year old males. Rock n roll, country, and pop music

Industry/Entity Type

ClipStreamo

Font styles to use
Sans Serif

Colors
0255a3
0792cd
ffffff
333333

Requirements
Must have
• Modern professional look

```html
<!DOCTYPE html>
<html lang="en">
<head>
<meta charset="utf-8">
<title>Fretmorning Academy – Lessons</title>
<link href="https://fonts.googleapis.com/css2?family=Playfair+Display:wght@400&family=Lato:wght@400;700&family=Roboto+Condensed:wght@400&display=swap" rel="stylesheet">
<style>
:root{
  --blue-dark:#0255a3;
  --blue:#0792cd;
  --white:#ffffff;
  --ink:#333333;
  --muted:#777777;
  --line:#e6e6e6;
  --page:#f2f2f2;
  --accent:#f7c300;
}
*{box-sizing:border-box;margin:0;padding:0}
html,body{width:1200px;height:1000px;overflow:hidden}
body{background:var(--page);font-family:'Lato',sans-serif;color:var(--ink);position:relative}
.abs{position:absolute}
.lesson-tag{display:flex;height:22px;font-family:'Roboto Condensed',sans-serif;color:var(--white);font-size:12px}
.lesson-tag .label{background:var(--blue-dark);padding:0 8px;line-height:22px;width:48px}
.lesson-tag .num{background:var(--blue);width:18px;text-align:center;line-height:20px;font-size:15px}
.card{background:var(--white);width:478px;box-shadow:0 1px 2px rgba(0,0,0,.06)}
.post-head{padding:8px 30px 0 32px;position:relative}
.badge{position:absolute;left:-20px;width:40px;height:40px;border-radius:50%;background:var(--accent);border:3px solid var(--white);box-shadow:0 0 0 1px #eee;display:flex;align-items:center;justify-content:center}
.post-title{font-family:'Playfair Display',serif;font-size:20px;line-height:26px;font-weight:400;color:#222}
.meta{display:flex;gap:18px;font-size:7.5px;color:var(--muted);text-transform:uppercase;margin-top:8px}
.meta span::before{content:"";display:inline-block;width:7px;height:7px;background:#999;border-radius:1px;margin-right:6px;vertical-align:-1px}
.body-card{padding:0 20px}
.lead{font-family:'Playfair Display',serif;font-size:12.4px;line-height:17px;color:#222}
.drop{float:left;font-family:'Playfair Display',serif;font-size:40px;line-height:36px;margin:2px 10px 0 10px}
.small{font-size:8.3px;line-height:16px;color:#444}
.share{display:flex;height:33px;border-top:1px solid var(--line);align-items:center;padding-left:24px;gap:17px;position:relative}
.share i{width:7px;height:7px;border-radius:50%;background:#333;display:block}
.share .go{position:absolute;right:0;top:0;width:36px;height:32px;border-left:1px solid var(--line);display:flex;align-items:center;justify-content:center}
.tweets{background:var(--white);width:230px;padding:6px 14px 0 24px;box-shadow:0 1px 2px rgba(0,0,0,.06)}
.tweet{position:relative;padding-left:22px;font-size:8.3px;line-height:15.5px;color:var(--muted);margin-bottom:4px}
.tweet::before{content:"";position:absolute;left:4px;top:4px;width:8px;height:7px;border-radius:50%;background:#444}
.tweet b{font-weight:400;color:#222}
.tweet .actions{color:#444;margin-top:2px;display:block}
.older{border:1px solid #ccc;background:var(--white);font-size:8.5px;padding:6px 9px;color:#444}
.footer{left:0;top:732px;width:1200px;height:268px;background:var(--white)}
.fcol h4{font-size:9.5px;font-weight:700;text-transform:uppercase;color:#111;display:flex;align-items:center;gap:7px}
.fcol h4::before{content:"";width:12px;height:7px;border-top:1px solid #666;border-bottom:1px solid #666;background:linear-gradient(#666,#666) center/100% 1px no-repeat}
.brand{display:flex;align-items:center;gap:6px;font-size:13px;font-weight:700;color:var(--blue-dark);margin:34px 0 14px}
.brand i{width:16px;height:16px;background:var(--blue-dark);display:block}
.about{font-size:8.4px;line-height:15.5px;color:#222;width:165px}
.tags{display:flex;flex-wrap:wrap;gap:8px 6px;width:160px;margin-top:20px}
.tags span{background:#f4f4f4;border:1px solid #e4e4e4;font-size:8px;color:#555;padding:0 13px;height:26px;line-height:25px}
.pop{display:flex;gap:8px;margin-top:15px}
.pop .thumb{width:49px;height:44px;flex:none}
.pop p{font-size:8.2px;line-height:12px;color:#222}
.pop small{display:block;font-size:6.5px;color:#777;margin-top:6px}
.ad{width:161px;height:161px;margin-top:23px;background:linear-gradient(160deg,#8fa6c7,#c9b49a 70%,#6d4f38);position:relative}
.ad p{position:absolute;left:0;bottom:0;font-family:'Playfair Display',serif;font-size:12px;line-height:16px;color:#111;background:rgba(255,255,255,.55);padding:0 2px}
</style>
</head>
<body>

<aside class="abs tweets" style="left:736px;top:0;height:288px">
  <div class="tweet">Lorem Ipsum has been the industry's standard dummy text ever since the 1500s, when an unknown printer took a <b>Lorem # Ipsum # standard #marketkit</b> <b>www.fretmorningacademy.example/</b><span class="actions">Reply · Retweet · Favorite</span></div>
  <div class="tweet">standard dummy text ever since the 1500s, when an unknown printer took a galley of type and scrambled it to make# <b>Lorem # Ipsum # standard #marketkit</b> <b>www.fretmorningacademy.example/</b><span class="actions">Reply · Retweet · Favorite</span></div>
  <div class="tweet">1500s, when an unknown printer took a galley of type and scrambled it to make# <b>Lorem # Ipsum # standard #marketkit</b> <b>www.fretmorningacademy.example/</b><span class="actions">Reply · Retweet · Favorite</span></div>
</aside>

<!-- Lesson 3 -->
<div class="abs lesson-tag" style="left:239px;top:15px"><span class="label">Lesson</span><span class="num">3</span></div>
<article class="abs card" style="left:239px;top:37px;height:89px">
  <div class="post-head">
    <div class="badge" style="top:12px"><svg width="14" height="14" viewBox="0 0 14 14"><path d="M5 2l7-1.5v8.5a2 2 0 1 1-1.4-1.9V3.2L6.4 4.1v6.4a2 2 0 1 1-1.4-1.9z" fill="#fff"/></svg></div>
    <h2 class="post-title">The Long Road Guitar Chords – The Lanterns – Video Guitar Lesson</h2>
    <div class="meta"><span>2 Mar 2015</span><span>0 Comments</span><span>Admin</span><span>1 Likes</span></div>
  </div>
</article>
<article class="abs card" style="left:239px;top:130px;height:273px">
  <div class="body-card" style="padding-top:48px">
    <p class="lead"><span class="drop">B</span>Lore sit amet dui ac lectus molestie porttitor. Aenean sagittis imperdiet massa. Nam est lacus consequat vitael semper tristique temp us in magna. Nullam site Aenean congue nunc viverra interdum aliquet lacus neque consectet der neque id ad piscing dolor leo nec metus. Fusce mattis, lectus ut semper Proin volutpat nisl ut tin cidunt Fusce quis neque vel leo Mauris non lectus sed erat.</p>
    <p class="small" style="margin-top:16px">Lore sit amet dui ac lectus molestie porttitor. Aenean sagittis imperdiet massa. Nam est lacus, consequat vitael semper tristique, temp us in magna. Nullam sit amet metus eget dolor semper laoreet. Aenean congue nunc viverra interdum aliquet lacus neque consectet der neque id adipiscing dolor leo nec metus ...</p>
  </div>
  <div class="share abs" style="left:0;right:0;top:240px"><i></i><i></i><i></i><i></i><i></i><i></i><span class="go"><svg width="12" height="6"><path d="M0 3h10M8 0.5l3 2.5-3 2.5" stroke="#222" fill="none"/></svg></span></div>
</article>

<!-- Lesson 4 -->
<div class="abs lesson-tag" style="left:239px;top:420px"><span class="label">Lesson</span><span class="num">4</span></div>
<article class="abs card" style="left:239px;top:441px;height:70px">
  <div class="post-head" style="padding-left:35px">
    <div class="badge" style="top:12px"><svg width="14" height="14" viewBox="0 0 14 14"><path d="M5 2l7-1.5v8.5a2 2 0 1 1-1.4-1.9V3.2L6.4 4.1v6.4a2 2 0 1 1-1.4-1.9z" fill="#fff"/></svg></div>
    <h2 class="post-title">Lead Me To The River Beginner Guitar Lesson – Corvell – Easy Chords</h2>
  </div>
</article>
<article class="abs card" style="left:239px;top:514px;height:111px">
  <div class="body-card" style="padding-top:18px"><p class="small">Cras sit amet dui ac lectus molestie porttitor. Aenean sagittis imperdiet massa. Nam est lacus, consequat vita eil semper tristique temp us in magna.</p></div>
  <div class="share abs" style="left:0;right:0;top:78px"><i></i><i></i><i></i><i></i><i></i><i></i><span class="go"><svg width="12" height="6"><path d="M0 3h10M8 0.5l3 2.5-3 2.5" stroke="#222" fill="none"/></svg></span></div>
</article>

<div class="abs older" style="left:239px;top:682px">Older Posts</div>

<footer class="abs footer">
  <section class="abs fcol" style="left:239px;top:34px">
    <h4>About Fretmorning Academy</h4>
    <div class="brand"><i></i>Fretmorning Academy</div>
    <p class="about">Cras sit amet dui acd lectus molestie portt Aenean sagit tisimp erdiet massa se. Namt acus consequat vitae semper trisque temp in magna. Nullam sit amet metus eget doli semp laoreet.</p>
  </section>
  <section class="abs fcol" style="left:425px;top:34px">
    <h4>Tags</h4>
    <div class="tags"><span>guitar</span><span>learn</span><span>free lesson</span><span>chords</span><span>beginner guitarist</span><span>music</span><span>get started</span><span>music</span><span>guitar chords</span><span>lesson</span></div>
  </section>
  <section class="abs fcol" style="left:611px;top:34px;width:170px">
    <h4>Popular Posts</h4>
    <div class="pop" style="margin-top:27px"><div class="thumb" role="img" aria-label="Photo of hands playing a guitar" style="background:linear-gradient(135deg,#6b5444,#cfc6bd)"></div><p>Suspendise lerisque lorem ipsu dum dolor<small>● ADMIN</small></p></div>
    <div class="pop" style="margin-top:8px"><div class="thumb" role="img" aria-label="Video still of a guitar fretboard" style="background:linear-gradient(135deg,#3f3a37,#a89a8c)"></div><p>Vestibulum auctor lacinia nunc etiam ipsum<small>● ADMIN</small></p></div>
    <div class="pop" style="margin-top:8px"><div class="thumb" style="background:#333;display:flex;align-items:center;justify-content:center"><svg width="14" height="14" viewBox="0 0 14 14"><path d="M5 2l7-1.5v8.5a2 2 0 1 1-1.4-1.9V3.2L6.4 4.1v6.4a2 2 0 1 1-1.4-1.9z" fill="#fff"/></svg></div><p>Quisque tincidunt lectus vel<small>● ADMIN</small></p></div>
  </section>
  <section class="abs fcol" style="left:797px;top:34px">
    <h4>Advertisment</h4>
    <div class="ad" role="img" aria-label="Photo of a guitarist playing an acoustic guitar"><p>Lead Me To The River Beginner<br>Corvell – Easy Chords</p></div>
  </section>
</footer>

</body>
</html>
```